Tri-fold brochue, business card, and stationary design.

Tri-fold brochure: We are looking to get a tri-fold brochure template created so we can add our content on each side of the brochure and then leave these with prospective clients during sales calls.Business card: We would like the business card to have employee name, phone number, and email address on the card. We are open to rounded corners as well.We just redid our website and we'd like all designs to be complementary to our new "Look and feel" of our website.

Contact Information for Business Card

We would like the business card to have employee name, phone number, and email address on the card. We are open to rounded corners as well.

We just redid our website and we'd like all designs to be complementary to our new "Look and feel" of our website.

```html
<!DOCTYPE html>
<html lang="en">
<head>
<meta charset="utf-8">
<title>Skyward Systems – Business Card</title>
<link rel="stylesheet" href="https://fonts.googleapis.com/css2?family=Exo+2:wght@700&family=Raleway:wght@400;600&display=swap">
<style>
  :root {
    --backdrop: #b4b2b7;
    --card: #ffffff;
    --card-tint: #f6f7f9;
    --brand-blue: #1a93d1;
    --brand-blue-faint: #e9f2fb;
    --accent-green: #8dc63f;
    --ink: #555558;
    --ink-soft: #666669;
  }
  * { margin: 0; padding: 0; box-sizing: border-box; }
  html, body { width: 1071px; height: 1200px; overflow: hidden; }
  body {
    background: var(--backdrop);
    position: relative;
    font-family: "Raleway", sans-serif;
  }
  .card {
    position: absolute;
    left: 198px;
    width: 674px;
    height: 436px;
    background: linear-gradient(135deg, var(--card-tint) 0%, var(--card) 45%, var(--card) 70%, var(--card-tint) 100%);
    overflow: hidden;
  }
  .card--front { top: 122px; }
  .card--back { top: 628px; }

  .brand {
    position: absolute;
    display: flex;
    align-items: center;
    gap: 26px;
  }
  .brand__dot {
    border-radius: 50%;
    background: var(--brand-blue);
    flex: none;
  }
  .brand__name {
    font-family: "Exo 2", sans-serif;
    font-weight: 700;
    color: var(--brand-blue);
    line-height: 1;
    white-space: nowrap;
  }
  .card--front .brand { left: 146px; top: 158px; }
  .card--front .brand__dot { width: 118px; height: 118px; }
  .card--front .brand__name { font-size: 40px; }

  .card--back .backdrop-disc {
    position: absolute;
    left: -40px;
    top: 80px;
    width: 310px;
    height: 380px;
    border-radius: 48% 48% 50% 50%;
    background: var(--brand-blue-faint);
  }
  .card--back .brand {
    left: 62px;
    top: 138px;
    flex-direction: column;
    gap: 20px;
    width: 170px;
  }
  .card--back .brand__dot { width: 92px; height: 92px; }
  .card--back .brand__name { font-size: 26px; text-align: center; white-space: normal; }

  .contact {
    position: absolute;
    left: 294px;
    top: 114px;
    list-style: none;
  }
  .contact__row {
    display: flex;
    align-items: center;
    gap: 18px;
    color: var(--ink-soft);
    font-size: 18px;
    height: 30px;
    margin-bottom: 11px;
  }
  .contact__row--person { align-items: flex-start; height: auto; margin-bottom: 44px; }
  .icon {
    width: 29px;
    height: 29px;
    border-radius: 50%;
    background: var(--accent-green);
    flex: none;
    display: flex;
    align-items: center;
    justify-content: center;
  }
  .icon svg { width: 17px; height: 17px; fill: #fff; }
  .person__name { font-weight: 600; font-size: 24px; color: var(--ink); line-height: 1.1; }
  .person__title { font-size: 18px; color: var(--ink-soft); margin-top: 6px; }
</style>
</head>
<body>

<section class="card card--front" aria-label="Card front">
  <div class="brand">
    <span class="brand__dot"></span>
    <span class="brand__name">Skyward Systems</span>
  </div>
</section>

<section class="card card--back" aria-label="Card back">
  <span class="backdrop-disc"></span>
  <div class="brand">
    <span class="brand__dot"></span>
    <span class="brand__name">Skyward Systems</span>
  </div>

  <ul class="contact">
    <li class="contact__row contact__row--person">
      <span class="icon"><svg viewBox="0 0 20 20"><circle cx="10" cy="6.5" r="4"/><path d="M3 18c0-4 3-6.5 7-6.5s7 2.5 7 6.5z"/></svg></span>
      <div>
        <div class="person__name">Employee Name</div>
        <div class="person__title">job title</div>
      </div>
    </li>
    <li class="contact__row">
      <span class="icon"><svg viewBox="0 0 20 20"><path d="M5 2l3 3.5-1.7 2.2c1 2.2 2.8 4 5 5l2.2-1.7L17 14l-2 3.5C8.5 17 3 11.5 2.5 5z"/></svg></span>
      <span>555-013-4827</span>
    </li>
    <li class="contact__row">
      <span class="icon"><svg viewBox="0 0 20 20"><path d="M2 5h16v10H2z" fill="none" stroke="#fff" stroke-width="1.8"/><path d="M2 5l8 6 8-6" fill="none" stroke="#fff" stroke-width="1.8"/></svg></span>
      <span>sales@skywardsystems.com</span>
    </li>
    <li class="contact__row">
      <span class="icon"><svg viewBox="0 0 20 20" fill="none" stroke="#fff" stroke-width="1.5"><circle cx="10" cy="10" r="7.5"/><ellipse cx="10" cy="10" rx="3.3" ry="7.5"/><path d="M2.5 10h15M4 6h12M4 14h12"/></svg></span>
      <span>www.skywardsystems.com</span>
    </li>
  </ul>
</section>

</body>
</html>
```